Business cards

We need business cards for the logo that you designed for our company. Something simple and clean.

Target Market(s)

Homeowners/ people looking for construction work

Industry/Entity Type

Construction

Contact Information for Business Card

Name: Doug Whitby, Number: 602-555-0174, Email: WhitbyBuildingCompany@mailbox-example.net ROC# 482063

Font styles to use
Serif

Colors

Designer to choose colors to be used in the design.

Requirements
Must have
• On one side of the card I would like to be all of the personal information I have put above along with the company logo that I have attached.
• On the other side of the card I would like the top half of the card to be the logo and then on the bottom half I would like to have the areas of construction we focus on along with an icon that represents it like the picture I have attached.
• Areas we focus on:
• Roofing, Kitchen and bath Remodel, Water Damage, Storm Damage, Fire Damage, Insurance Specialist
• If we could arrange those in alphabetical order.
Nice to have
• I have added 2 company logos a colorful one and a black one it would be nice to see a couple different options the black logo to be more simple and sleek and the colorful logo to be more colorful

```html
<!DOCTYPE html>
<html lang="en">
<head>
<meta charset="utf-8">
<title>Whitby Building Company – Business Cards</title>
<link href="https://fonts.googleapis.com/css2?family=Montserrat:wght@400;500;600;700&family=Oswald:wght@500&display=swap" rel="stylesheet">
<style>
  :root{
    --backdrop:#1c1c1d;
    --card:#161617;
    --card-edge:#202022;
    --blue:#2aa7e0;
    --red:#e3242b;
    --white:#f1f1f1;
    --muted:#cfcfcf;
    --pin-green:#7cb342;
    --pin-light:#e8efe0;
  }
  *{margin:0;padding:0;box-sizing:border-box}
  html,body{width:1200px;height:900px;overflow:hidden;background:var(--backdrop)}
  .canvas{position:relative;width:1200px;height:900px;font-family:"Montserrat",sans-serif;color:var(--white)}
  .card{
    position:absolute;left:250px;width:700px;height:400px;
    background:linear-gradient(135deg,var(--card-edge),var(--card));
    overflow:hidden;
  }
  .card::after{content:"";position:absolute;left:0;right:0;bottom:0;height:8px;background:var(--blue)}
  .card-front{top:40px}
  .card-back{top:470px}

  /* Front */
  .brand{
    position:absolute;top:56px;left:0;right:0;text-align:center;
    font-family:"Montserrat",sans-serif;font-weight:600;font-size:34px;line-height:1.1;
    letter-spacing:2px;color:var(--blue);text-transform:uppercase;white-space:nowrap;
  }
  .services{
    position:absolute;top:128px;left:0;right:0;text-align:center;
    font-size:14px;font-weight:500;letter-spacing:1.5px;line-height:1.6;
    text-transform:uppercase;color:var(--white);
  }
  .focus-list{
    position:absolute;top:220px;left:40px;right:40px;
    display:flex;justify-content:space-between;list-style:none;
  }
  .focus-item{width:110px;text-align:center;text-transform:uppercase}
  .focus-item svg{width:46px;height:56px;display:block;margin:0 auto 6px}
  .focus-title{display:block;font-weight:700;font-size:13px;letter-spacing:.5px}
  .focus-sub{display:block;font-weight:500;font-size:10px;letter-spacing:.5px;color:var(--muted)}
  .focus-item.is-active .focus-sub{border-bottom:2px solid var(--pin-green);padding-bottom:6px}

  /* Back */
  .identity{position:absolute;top:150px;right:440px;text-align:right}
  .person-name{
    font-family:"Oswald",sans-serif;font-weight:500;font-size:42px;
    color:var(--blue);text-transform:uppercase;letter-spacing:.5px;line-height:1;
  }
  .person-role{font-size:19px;font-weight:400;margin-top:6px}
  .divider{position:absolute;left:280px;top:150px;width:2px;height:66px;background:var(--blue)}
  .contact{position:absolute;left:300px;top:148px;list-style:none}
  .contact li{display:flex;align-items:center;gap:10px;font-size:13.5px;letter-spacing:.4px;line-height:24px;white-space:nowrap}
  .contact svg{width:12px;height:12px;flex:none}
  .licence{position:absolute;left:0;right:0;top:315px;text-align:center;font-size:18px;letter-spacing:1px}
  .licence-label{color:var(--blue)}
</style>
</head>
<body>
<main class="canvas">

  <section class="card card-front" aria-label="Card front">
    <h1 class="brand">Whitby Building Company</h1>
    <p class="services">
      Roofing - Kitchen and Bath Remodel - Water Damage<br>
      Storm Damage - Fire Damage - Insurance Specialist
    </p>
    <ul class="focus-list">
      <li class="focus-item">
        <svg viewBox="0 0 46 56" aria-hidden="true">
          <path d="M23 54 L9 38 A20 20 0 1 1 37 38 Z" fill="var(--pin-green)"/>
          <circle cx="23" cy="23" r="16" fill="var(--pin-light)"/>
          <path d="M23 12 C19 19 16 22 16 26 a7 7 0 0 0 14 0 c0-4-3-7-7-14z" fill="#2a4fa8"/>
        </svg>
        <span class="focus-title">Water</span><span class="focus-sub">Damage</span>
      </li>
      <li class="focus-item is-active">
        <svg viewBox="0 0 46 56" aria-hidden="true">
          <path d="M23 54 L9 38 A20 20 0 1 1 37 38 Z" fill="var(--pin-green)"/>
          <circle cx="23" cy="23" r="16" fill="var(--pin-light)"/>
          <path d="M24 11 c2 6 8 9 8 16 a9 9 0 0 1-18 0 c0-4 3-6 4-9 c1 3 2 4 3 4 c1-4 2-7 3-11z" fill="#d9381e"/>
        </svg>
        <span class="focus-title">Fire</span><span class="focus-sub">Damage</span>
      </li>
      <li class="focus-item">
        <svg viewBox="0 0 46 56" aria-hidden="true">
          <path d="M23 54 L9 38 A20 20 0 1 1 37 38 Z" fill="var(--pin-green)"/>
          <circle cx="23" cy="23" r="16" fill="var(--pin-light)"/>
          <g fill="#3f6b2a"><circle cx="18" cy="18" r="3"/><circle cx="26" cy="16" r="3"/><circle cx="29" cy="24" r="3"/><circle cx="21" cy="26" r="3"/><circle cx="16" cy="31" r="2.5"/><circle cx="26" cy="31" r="2.5"/></g>
        </svg>
        <span class="focus-title">Mold</span><span class="focus-sub">Remediation</span>
      </li>
      <li class="focus-item">
        <svg viewBox="0 0 46 56" aria-hidden="true">
          <path d="M23 54 L9 38 A20 20 0 1 1 37 38 Z" fill="var(--pin-green)"/>
          <circle cx="23" cy="23" r="16" fill="var(--pin-light)"/>
          <path d="M14 24 a5 5 0 0 1 5-6 a7 7 0 0 1 13 2 a4 4 0 0 1 0 8 h-14 a4 4 0 0 1-4-4z" fill="#4a6fa5"/>
          <path d="M24 28 l-3 6 h3 l-2 5 l5-7 h-3 l2-4z" fill="#f2c230"/>
        </svg>
        <span class="focus-title">Storm</span><span class="focus-sub">Damage</span>
      </li>
      <li class="focus-item">
        <svg viewBox="0 0 46 56" aria-hidden="true">
          <path d="M23 54 L9 38 A20 20 0 1 1 37 38 Z" fill="var(--pin-green)"/>
          <circle cx="23" cy="23" r="16" fill="var(--pin-light)"/>
          <rect x="13" y="13" width="20" height="20" fill="#ef8a2b"/>
          <g fill="#fbd9b0"><rect x="16" y="16" width="3" height="3"/><rect x="21.5" y="16" width="3" height="3"/><rect x="27" y="16" width="3" height="3"/><rect x="16" y="22" width="3" height="3"/><rect x="21.5" y="22" width="3" height="3"/><rect x="27" y="22" width="3" height="3"/></g>
        </svg>
        <span class="focus-title">Commercial</span><span class="focus-sub">Services</span>
      </li>
    </ul>
  </section>

  <section class="card card-back" aria-label="Card back">
    <div class="identity">
      <p class="person-name">Doug Whitby</p>
      <p class="person-role">Director</p>
    </div>
    <span class="divider"></span>
    <ul class="contact">
      <li>
        <svg viewBox="0 0 12 12" aria-hidden="true"><path d="M3 1 l2 2.5 -1.2 1.2 a6 6 0 0 0 3.5 3.5 L8.5 7 11 9 9.5 11 C5 10.5 1.5 7 1 2.5z" fill="var(--blue)"/></svg>
        602-555-0174
      </li>
      <li>
        <svg viewBox="0 0 12 12" aria-hidden="true"><rect x="1" y="2.5" width="10" height="7" fill="none" stroke="var(--blue)" stroke-width="1.2"/><path d="M1 2.5 L6 6.5 11 2.5" fill="none" stroke="var(--blue)" stroke-width="1.2"/></svg>
        WhitbyBuildingCompany@mailbox-example.net
      </li>
      <li>
        <svg viewBox="0 0 12 12" aria-hidden="true"><circle cx="6" cy="6" r="5" fill="none" stroke="var(--blue)" stroke-width="1.1"/><ellipse cx="6" cy="6" rx="2.2" ry="5" fill="none" stroke="var(--blue)" stroke-width="1"/><path d="M1 6 H11" stroke="var(--blue)" stroke-width="1"/></svg>
        www.whitbybuilding-example.com
      </li>
    </ul>
    <p class="licence"><span class="licence-label">ROC#</span> 482063</p>
  </section>

</main>
</body>
</html>
```